Kestrel Wiring - Electrician company flyers for new clients

I want a flyer that will be dropped into mailboxes and will hopefully stand out more that the ones i have tried to mock up. I have attached my latest design to give you an idea but it is rather boring.

The aim is obviously to entice new customers into calling me for any electrical work, mainly domestic but i also do commercial work.
I will also upload a photo of my business card so that it can be used as a reference and my website is www.kestrelwiring.co.nz for any extra information.

Ideally the flyer will be DL size
measurements from printmorrow is that's any help
Document Trim Size
99 x 210 mm
1169 x 2480 pixels
Full Bleed Size
102 x 213 mm
1205 x 2516 pixels

Target Market(s)

Domestic electrical works

Industry/Entity Type

Electrician

Requirements
Must have
• all of my contact details -
• Dean Forsyth
• Dean@kestrelwiring.co.nz
• 027 3815 942
• www.kestrelwiring.co.nz
• A little write up similar to the one written on my draft but there's probably alot of room for improvement as my writing skills are lacking.
Nice to have
• clear and concise writing so that people wont throw it away before reading

```html
<!DOCTYPE html>
<html lang="en">
<head>
<meta charset="utf-8">
<title>Kestrel Wiring – Flyer</title>
<link href="https://fonts.googleapis.com/css2?family=Roboto+Condensed:wght@400;700;800&family=Open+Sans:wght@400;600&display=swap" rel="stylesheet">
<style>
  :root{
    --blue:#1f7fd0;
    --blue-light:#3fa3e8;
    --blue-deep:#0f4f96;
    --navy:#0b3a73;
    --white:#ffffff;
  }
  *{box-sizing:border-box;margin:0;padding:0}
  html,body{width:719px;height:1200px;overflow:hidden;background:#f2f2f2}
  .flyer{position:relative;width:719px;height:1200px;background:linear-gradient(180deg,var(--blue-light) 45%,var(--blue) 70%,var(--blue-deep) 100%);overflow:hidden;font-family:"Open Sans",Arial,sans-serif;color:var(--white)}
  .brand{position:absolute;top:0;left:0;width:100%;height:175px;background:var(--white);display:flex;align-items:center;justify-content:center;gap:18px}
  .brand-mark{width:34px;height:34px;background:var(--blue)}
  .brand-name{font-family:"Roboto Condensed",Arial,sans-serif;font-weight:800;font-size:66px;letter-spacing:2px;color:var(--blue);text-transform:uppercase;line-height:1}
  .hero{position:absolute;top:160px;left:0;width:719px;height:440px}
  .headline{position:absolute;top:622px;left:0;width:100%;text-align:center;font-family:"Roboto Condensed",Arial,sans-serif;font-weight:700;font-size:44px;line-height:1.12;text-transform:uppercase}
  .intro{position:absolute;top:738px;left:50px;width:619px;text-align:center;font-size:19px;line-height:1.42}
  .services{position:absolute;top:868px;left:30px;width:659px;display:flex;justify-content:space-between;list-style:none}
  .service{width:120px;text-align:center;font-family:"Roboto Condensed",Arial,sans-serif;font-size:12px;line-height:1.2;text-transform:uppercase}
  .service-icon{display:block;margin:0 auto 8px;width:54px;height:54px}
  .quote-bar{position:absolute;top:995px;left:50px;width:619px;height:66px;background:var(--white);border-radius:8px;display:flex;align-items:center;justify-content:center;gap:20px;font-family:"Roboto Condensed",Arial,sans-serif;font-weight:700;font-size:38px;color:var(--blue-deep)}
  .quote-bar .label{text-transform:uppercase}
  .phone-icon{width:40px;height:40px}
  .contact-strip{position:absolute;bottom:0;left:0;width:100%;height:110px;background:var(--white);color:var(--navy);display:flex;flex-direction:column;align-items:center;justify-content:center;gap:6px}
  .contact-name{font-family:"Roboto Condensed",Arial,sans-serif;font-weight:700;font-size:22px;text-transform:uppercase;letter-spacing:1px}
  .contact-lines{display:flex;gap:16px;font-size:19px}
  .divider{opacity:.6}
</style>
</head>
<body>
<main class="flyer">
  <header class="brand">
    <span class="brand-mark"></span>
    <span class="brand-name">Kestrel Wiring</span>
  </header>

  <svg class="hero" viewBox="0 0 719 440" xmlns="http://www.w3.org/2000/svg">
    <defs>
      <linearGradient id="photoTone" x1="0" y1="0" x2="1" y2="0">
        <stop offset="0" stop-color="#eef0f1"/>
        <stop offset=".45" stop-color="#d3d9de"/>
        <stop offset=".7" stop-color="#2f6fb8"/>
        <stop offset="1" stop-color="#dfe3e6"/>
      </linearGradient>
      <linearGradient id="toolTone" x1="0" y1="0" x2="1" y2="1">
        <stop offset="0" stop-color="#f2c230"/>
        <stop offset="1" stop-color="#3a3f46"/>
      </linearGradient>
      <clipPath id="heroClip"><path d="M0 0H719V330Q360 440 0 330Z"/></clipPath>
    </defs>
    <rect width="719" height="440" fill="url(#photoTone)" clip-path="url(#heroClip)" role="img" aria-label="Photo of an electrician in blue overalls holding a cable coil in a bright modern kitchen"/>
    <path d="M0 330Q360 440 719 330" fill="none" stroke="#ffffff" stroke-width="10"/>
    <path d="M0 345Q360 452 719 345" fill="none" stroke="#0f4f96" stroke-width="6" opacity=".6"/>
    <circle cx="95" cy="340" r="52" fill="url(#toolTone)" stroke="#fff" stroke-width="6" role="img" aria-label="Close-up photo of a multimeter testing wires"/>
    <circle cx="185" cy="360" r="48" fill="url(#toolTone)" stroke="#fff" stroke-width="6" role="img" aria-label="Close-up photo of hands working on an electrical panel"/>
  </svg>

  <h1 class="headline">Do you need a local and<br>reliable electrician?</h1>
  <p class="intro">Specializing in residential and commercial electrical services, we are dedicated to providing customer service that is second to none. Whether you need a small wiring fix or the full installation, we can get the job done right.</p>

  <ul class="services">
    <li class="service">
      <svg class="service-icon" viewBox="0 0 54 54"><circle cx="27" cy="27" r="25" fill="none" stroke="#fff" stroke-width="2.5"/><path d="M15 28L27 17L39 28M19 25V38H35V25" fill="none" stroke="#fff" stroke-width="2.5"/></svg>
      Residential<br>electric
    </li>
    <li class="service">
      <svg class="service-icon" viewBox="0 0 54 54"><circle cx="27" cy="27" r="25" fill="none" stroke="#fff" stroke-width="2.5"/><rect x="18" y="15" width="18" height="24" fill="none" stroke="#fff" stroke-width="2.5"/><path d="M22 20h3M29 20h3M22 26h3M29 26h3M22 32h3M29 32h3" stroke="#fff" stroke-width="2"/></svg>
      Commercial<br>electric
    </li>
    <li class="service">
      <svg class="service-icon" viewBox="0 0 54 54"><circle cx="27" cy="27" r="25" fill="none" stroke="#fff" stroke-width="2.5"/><rect x="17" y="15" width="20" height="24" rx="2" fill="none" stroke="#fff" stroke-width="2.5"/><path d="M22 21v6M27 21v6M32 21v6M21 33h12" stroke="#fff" stroke-width="2.5"/></svg>
      Panel<br>upgrades
    </li>
    <li class="service">
      <svg class="service-icon" viewBox="0 0 54 54"><circle cx="27" cy="27" r="25" fill="none" stroke="#fff" stroke-width="2.5"/><circle cx="27" cy="27" r="8" fill="none" stroke="#fff" stroke-width="2.5"/><path d="M27 13v5M27 36v5M13 27h5M36 27h5M17 17l4 4M33 33l4 4M37 17l-4 4M21 33l-4 4" stroke="#fff" stroke-width="2.5"/></svg>
      Service<br>changes
    </li>
    <li class="service">
      <svg class="service-icon" viewBox="0 0 54 54"><circle cx="27" cy="27" r="25" fill="none" stroke="#fff" stroke-width="2.5"/><path d="M17 28l7 7l13-15" fill="none" stroke="#fff" stroke-width="3"/></svg>
      No job too big<br>or too small
    </li>
  </ul>

  <div class="quote-bar">
    <span class="label">Free quote</span>
    <svg class="phone-icon" viewBox="0 0 40 40"><circle cx="20" cy="20" r="18" fill="none" stroke="#0f4f96" stroke-width="2.5"/><path d="M14 11c-2 1-3 3-2 6c2 6 6 10 12 12c3 1 5 0 6-2l-4-4l-3 2c-3-1-5-4-6-6l2-3z" fill="#0f4f96"/></svg>
    <span class="number">027 3815 942</span>
  </div>

  <footer class="contact-strip">
    <span class="contact-name">Dean Forsyth</span>
    <div class="contact-lines">
      <span>Dean@kestrelwiring.co.nz</span>
      <span class="divider">|</span>
      <span>www.kestrelwiring.co.nz</span>
    </div>
  </footer>
</main>
</body>
</html>
```